Corewise Motion Business Cards

Can all designers please apply the following info on their designs' back-side of the business card: (please see brief file upload ('Info for backside...' - for required info, colours & layout)

SPECIALISING IN INDIVIDUAL PILATES INSTRUCTION
MATWORK – including small apparatus
and STUDIO:
VIVANTE 5 REFORMER
LADDER BARREL
MERIDAN BARREL
TENDRA DOME
KALVO CHAIR
TOR-I-VAN

Business Cards for Corewise Motion - applying the Corewise Motion logo design selected earlier.
Note the business card requires both a front and back side. Please refer to two uploaded ppt-files for type of info required to be displayed, and rough position of where info could be. Require innovative / fresh approach to business card design and use of colour by designers now. Please refer to and use logo as uploaded - also for potential business card colour application.

Dear Designers,

Please note the additional inclusion / upload of two draft ppt-files that try to show where I want what type of information, for both the front & back sides of the required business card, plus an attempt at showing the high-level concept / idea of business info position.

As my 'drafts' obviously lack colour and any ability towards innovative card design or approach – I now rely on your vastly superior graphic design abilities to produce a really great business card for my business…

Looking forward to your submissions!

Kind regards, Maren for: Corewise Motion 

Hello all Designers,

Can all designers please apply the following info on their designs' back-side of the business card: (please see / refer to the Brief and specifically the file upload ('Info for backside...' - for required info, colours & layout) - for the backside of the business card).

Info content (without colour, layout etc.):

and STUDIO:

VIVANTE 5 REFORMER

LADDER BARREL

MERIDAN BARREL

TENDRA DOME

KALVO CHAIR

TOR-I-VAN

Thank you to all designers that submitted for consideration!

With regards,

Corewise Motion

```html
<!DOCTYPE html>
<html lang="en">
<head>
<meta charset="utf-8">
<title>Corewise Motion – Business Cards</title>
<link href="https://fonts.googleapis.com/css2?family=Questrial&family=Montserrat:wght@600;700&display=swap" rel="stylesheet">
<style>
  :root {
    --backdrop: #a9aaac;
    --card: #ffffff;
    --green: #4f7a23;
    --orange: #e0601e;
    --ink: #3a3a3a;
    --muted: #555555;
    --rule: #b9b9b9;
  }
  * { margin: 0; padding: 0; box-sizing: border-box; }
  html, body { width: 1200px; height: 871px; overflow: hidden; }
  body {
    background: var(--backdrop);
    font-family: "Questrial", Arial, sans-serif;
    position: relative;
  }
  .card {
    position: absolute;
    width: 520px;
    height: 298px;
    background: var(--card);
    box-shadow: 0 6px 16px rgba(0,0,0,0.25);
    overflow: hidden;
  }
  .card--back { left: 90px; top: 110px; }
  .card--front { left: 590px; top: 450px; }

  .brand-dot {
    width: 30px; height: 30px; border-radius: 50%;
    background: var(--green);
    flex: none;
  }
  .brand-name {
    font-family: "Questrial", Arial, sans-serif;
    color: var(--orange);
    line-height: 1;
    white-space: nowrap;
  }

  /* Back side */
  .back-brand {
    position: absolute;
    left: 34px; top: 96px;
    width: 196px;
    display: flex; flex-direction: column; align-items: center; gap: 12px;
  }
  .back-brand .brand-dot { width: 44px; height: 44px; }
  .back-brand .brand-name { font-size: 25px; }
  .services {
    position: absolute;
    left: 262px; top: 30px;
    width: 244px;
    color: var(--green);
    font-family: "Montserrat", Arial, sans-serif;
    font-weight: 600;
    font-size: 7.8px;
    letter-spacing: 0.02em;
    line-height: 2.3;
    white-space: nowrap;
  }
  .equipment {
    list-style: none;
    margin-top: 6px;
    font-family: "Questrial", Arial, sans-serif;
    font-weight: 400;
    color: var(--orange);
    font-size: 10.5px;
    letter-spacing: 0.06em;
    line-height: 1.6;
  }
  .equipment li {
    display: flex; align-items: center; gap: 10px;
    margin: 0 0 7px 10px;
  }
  .equipment li::before {
    content: "";
    width: 10px; height: 10px; border-radius: 50%;
    background: var(--green);
    flex: none;
  }

  /* Front side */
  .front-brand {
    position: absolute;
    left: 30px; top: 28px;
  }
  .front-brand .brand-row { display: flex; align-items: center; gap: 12px; }
  .front-brand .brand-name { font-size: 32px; }
  .tagline {
    margin: 8px 0 0 42px;
    font-family: "Montserrat", Arial, sans-serif;
    font-weight: 700;
    font-size: 10.5px;
    letter-spacing: 0.16em;
    color: var(--green);
    white-space: nowrap;
  }
  .holder {
    position: absolute;
    left: 30px; top: 122px;
    width: 300px;
  }
  .holder-name {
    font-family: "Montserrat", Arial, sans-serif;
    font-weight: 700;
    font-size: 12px;
    letter-spacing: 0.08em;
    color: var(--ink);
  }
  .holder-title {
    margin-top: 3px;
    font-size: 10.5px;
    letter-spacing: 0.06em;
    color: var(--orange);
    padding-bottom: 8px;
    border-bottom: 1px solid var(--rule);
    white-space: nowrap;
  }
  .address {
    position: absolute;
    left: 30px; top: 178px;
    font-size: 10.5px;
    line-height: 1.75;
    letter-spacing: 0.06em;
    color: var(--muted);
    font-style: normal;
  }
  .contacts {
    position: absolute;
    left: 192px; top: 208px;
    list-style: none;
    font-size: 10.5px;
    letter-spacing: 0.06em;
    color: var(--muted);
    white-space: nowrap;
  }
  .contacts li { display: flex; align-items: center; gap: 12px; margin-bottom: 7px; }
  .contacts svg { width: 12px; height: 12px; flex: none; }
  .edge-band { position: absolute; right: 0; top: 0; width: 110px; height: 298px; }
</style>
</head>
<body>

  <section class="card card--back" aria-label="Business card, back side">
    <div class="back-brand">
      <span class="brand-dot"></span>
      <span class="brand-name">Corewise Motion</span>
    </div>
    <div class="services">
      <p>SPECIALISING IN INDIVIDUAL PILATES INSTRUCTION</p>
      <p>MATWORK (INCL. SMALL APPARATUS)</p>
      <p>STUDIO:</p>
      <ul class="equipment">
        <li>VIVANTE 5 REFORMER</li>
        <li>LADDER BARREL</li>
        <li>MERIDAN BARREL</li>
        <li>TENDRA DOME</li>
        <li>KALVO CHAIR</li>
        <li>TOR-I-VAN</li>
      </ul>
    </div>
  </section>

  <section class="card card--front" aria-label="Business card, front side">
    <svg class="edge-band" viewBox="0 0 110 298" preserveAspectRatio="none" aria-hidden="true">
      <path d="M60 0 H110 V298 H20 C70 230 40 120 60 0 Z" fill="var(--green)"/>
      <path d="M20 298 C70 230 40 120 60 0 L54 0 C34 120 62 228 10 298 Z" fill="var(--orange)"/>
    </svg>

    <div class="front-brand">
      <div class="brand-row">
        <span class="brand-dot"></span>
        <span class="brand-name">Corewise Motion</span>
      </div>
      <p class="tagline">BALANCE - STRENGTH - FLEXIBILITY</p>
    </div>

    <div class="holder">
      <p class="holder-name">MAREN HOLLSTEIN</p>
      <p class="holder-title">DIPLOMA OF PROFESSIONAL PILATES INSTRUCTION</p>
    </div>

    <address class="address">
      STUDIO LOCATION:<br>
      12 FERNCREST AVENUE<br>
      LARKFIELD WA 6099
    </address>

    <ul class="contacts">
      <li>
        <svg viewBox="0 0 12 12" aria-hidden="true"><path d="M2 1.5 L4 1 L5 3.5 L3.8 4.5 C4.5 6 6 7.5 7.5 8.2 L8.5 7 L11 8 L10.5 10 C6 10.5 1.5 6 2 1.5 Z" fill="var(--orange)"/></svg>
        041 555 0192
      </li>
      <li>
        <svg viewBox="0 0 12 12" aria-hidden="true"><rect x="1" y="2.5" width="10" height="7" fill="none" stroke="var(--orange)" stroke-width="1.2"/><path d="M1 2.5 L6 6.5 L11 2.5" fill="none" stroke="var(--orange)" stroke-width="1.2"/></svg>
        INFO@COREWISEMOTION.COM
      </li>
      <li>
        <svg viewBox="0 0 12 12" aria-hidden="true"><circle cx="6" cy="6" r="5" fill="none" stroke="var(--orange)" stroke-width="1.2"/><path d="M1 6 H11 M6 1 C3.5 4 3.5 8 6 11 M6 1 C8.5 4 8.5 8 6 11" fill="none" stroke="var(--orange)" stroke-width="1"/></svg>
        WWW.COREWISEMOTION.COM.AU
      </li>
    </ul>
  </section>

</body>
</html>
```